50 years of Beat (birthday party)

I need a flyer that I can send to all guests as ChatLoop.
Also as a digital file (e.g. PDF). Thanks!
Occasion: Beat's 50th birthday
It's a birthday party for family and friends
Location: Marquee at the football field, 8890 Flums
Live music
Bar pub
Murrow
Date: Saturday, May 25, 2024
Time: from 2 p.m. until open-end
Flexible participation - come and go as you please
Registration or deregistration: ChatLoop on 078 - 312 65 17

Please create a flyer as an invitation. I want an Irish rock style with a touch of “Schlager” :-). There should be a real party.
Attention: no heavy metal style!!
It would be cool if a rock guitar and/or microphone were included.
Otherwise, I'm free and happy to be surprised. The flyer should not be too childish or youthful. There are practically no children at the event.

Additionally, please send a simpler flyer than “Save the date”.
Just the date and occasion.
Without place, time and registration.
With the note: Update follows...
The design is the same as the flyer with registration.
Updates

It would be cool if the Murrow logo was visible too.
A whiskey glass would also be possible.
Balloons are not absolutely necessary - it looks like a children's party.
Please make the flyers rocky.

Target Market(s)

Family & Friends

Industry/Entity Type

look

Font styles to use
Other font styles liked:
• rockig

Colors

Designer to choose colors to be used in the design.

Requirements
Must have
• Irish rock design
Nice to have
• Rock guitar would be cool
Should not have
• comics

```html
<!DOCTYPE html>
<html lang="en">
<head>
<meta charset="utf-8">
<title>Beat's 50th Birthday – Save the Date</title>
<link rel="stylesheet" href="https://fonts.googleapis.com/css2?family=Archivo+Black&family=Archivo+Narrow:wght@700&family=Montserrat:wght@300;700&family=Yellowtail&display=swap">
<style>
  :root{
    --backdrop:#17501b;
    --card:#010d03;
    --glow:#0a5a14;
    --green:#7ab648;
    --frame:#5f9a3d;
    --white:#ffffff;
  }
  *{margin:0;padding:0;box-sizing:border-box}
  html,body{width:1200px;height:1200px;overflow:hidden;background:var(--backdrop)}
  .flyer{
    position:absolute;left:233px;top:80px;width:733px;height:1040px;
    background:radial-gradient(ellipse 340px 420px at 330px 560px,#053c0c 0%,#02260a 45%,var(--card) 100%);
    overflow:hidden;
  }
  .frame{position:absolute;inset:0;width:733px;height:1040px}
  .frame rect{fill:none;stroke:var(--frame)}
  .corner{position:absolute;width:78px;height:78px;background:radial-gradient(circle,rgba(95,154,61,.35),rgba(95,154,61,.1) 65%,transparent 70%)}
  .corner.tl{left:36px;top:40px}.corner.tr{right:36px;top:40px}
  .corner.bl{left:36px;bottom:40px}.corner.br{right:36px;bottom:40px}
  .guitar-photo{
    position:absolute;left:300px;top:240px;width:330px;height:560px;
    background:radial-gradient(ellipse 150px 180px at 130px 420px,rgba(18,130,36,.55) 0%,rgba(10,90,20,.25) 55%,transparent 80%);
  }
  .txt{position:absolute;line-height:1;white-space:nowrap;transform-origin:left top}
  .intro{left:0;width:733px;text-align:center;top:130px;font:300 18px "Montserrat",sans-serif;letter-spacing:.38em;color:var(--white)}
  .intro-sub{left:0;width:733px;text-align:center;top:153px;font:700 18px "Montserrat",sans-serif;letter-spacing:.26em;color:var(--green)}
  .wide{font-family:"Archivo Black",sans-serif;font-weight:400}
  .narrow{font-family:"Archivo Narrow",sans-serif;font-weight:700}
  .name{left:159px;top:211px;font-size:66px;color:var(--green);transform:scaleX(1.05)}
  .age{left:158px;top:284px;font-size:98px;color:var(--white);transform:scaleX(1.38)}
  .age-suffix{left:361px;top:266px;font-size:64px;color:var(--white);transform:scaleX(1.2)}
  .occasion{left:150px;top:372px;font:400 112px "Yellowtail",cursive;color:var(--green);transform:rotate(-18deg);transform-origin:left center}
  .day{left:174px;top:526px;font-size:50px;color:var(--white)}
  .month{left:173px;top:574px;font-size:70px;color:var(--green)}
  .date{left:174px;top:633px;font-size:64px;color:var(--white);transform:scaleX(1.2)}
  .year{left:173px;top:693px;font-size:62px;color:var(--green)}
  .rule{position:absolute;height:0;border-top:3px dotted rgba(122,182,72,.55)}
  .rule.one{left:176px;top:773px;width:175px}
  .rule.two{left:171px;top:914px;width:376px}
  .save{left:175px;top:790px;font-size:54px;color:var(--white);transform:scaleX(1.3)}
  .save-sub{left:175px;top:843px;font-size:54px;color:var(--green);transform:scaleX(1.3)}
</style>
</head>
<body>
<main class="flyer">
  <svg class="frame" viewBox="0 0 733 1040" aria-hidden="true">
    <rect x="53" y="58" width="627" height="923" stroke-width="2"/>
    <rect x="62" y="67" width="609" height="905" stroke-width="1.5"/>
    <rect x="71" y="76" width="591" height="887" stroke-width="2"/>
  </svg>
  <div class="corner tl" role="img" aria-label="Celtic knot corner ornament"></div>
  <div class="corner tr" role="img" aria-label="Celtic knot corner ornament"></div>
  <div class="corner bl" role="img" aria-label="Celtic knot corner ornament"></div>
  <div class="corner br" role="img" aria-label="Celtic knot corner ornament"></div>

  <div class="guitar-photo" role="img" aria-label="Photo of a green electric rock guitar leaning diagonally with a glass of whiskey on ice at its base"></div>

  <p class="txt intro">IT'S A BIRTHDAY PARTY FOR</p>
  <p class="txt intro-sub">FAMILY AND FRIENDS</p>

  <h1 class="txt wide name">BEAT'S</h1>
  <p class="txt wide age">50</p>
  <p class="txt wide age-suffix">TH</p>
  <p class="txt occasion">Birthday</p>

  <p class="txt narrow day">SATURDAY</p>
  <p class="txt narrow month">MAY</p>
  <p class="txt wide date">25</p>
  <p class="txt narrow year">2024</p>

  <div class="rule one"></div>
  <p class="txt wide save">SAVE</p>
  <p class="txt wide save-sub">THE DATE</p>
  <div class="rule two"></div>
</main>
</body>
</html>
```